Create a professional, eye-catching business card design that reflects the values and services of Brookfern Veterinary Hospital. we provide veterinary services and the business card should be a memorable representation of the clinic and align with its branding and mission. our tag line is "Life Long Companions, Lifelong Care"
Use clean, modern typography. Prioritize readability and professionalism. We would like to see designs that use the color blue, as in the logo example. the final design should communicate professionalism and care, with attention to detail.

```html
<!DOCTYPE html>
<html lang="en">
<head>
<meta charset="utf-8">
<title>Brookfern Veterinary Hospital – Business Card</title>
<link href="https://fonts.googleapis.com/css2?family=Lato:wght@400;700;900&display=swap" rel="stylesheet">
<style>
  :root {
    --stage: #3b3b3b;
    --navy: #1c3461;
    --navy-pattern: #22406f;
    --edge: #4d82c6;
    --paper: #ececec;
    --ink: #1a1a1a;
    --sky: #4cc3f0;
    --white: #ffffff;
  }
  * { margin: 0; padding: 0; box-sizing: border-box; }
  html, body {
    width: 1200px; height: 1000px; overflow: hidden;
    background: var(--stage);
    font-family: "Lato", sans-serif;
  }
  .canvas { position: relative; width: 1200px; height: 1000px; }
  .card {
    position: absolute; left: 228px; width: 788px; height: 448px;
    border-radius: 28px; border: 2px solid var(--edge); overflow: hidden;
  }
  .card-front { top: 26px; background: var(--navy); }
  .card-back { top: 500px; background: var(--paper); }

  .front-pattern {
    position: absolute; inset: 0;
    background: linear-gradient(135deg, var(--navy-pattern), var(--navy) 60%, var(--navy-pattern));
  }
  .front-brand {
    position: absolute; left: 0; right: 0; top: 150px;
    display: flex; flex-direction: column; align-items: center; gap: 8px;
    color: var(--white); font-weight: 900; text-align: center;
  }
  .front-brand .mark-dot {
    width: 62px; height: 62px; border-radius: 50%; border: 2px solid var(--white);
  }
  .front-brand .brand-name { font-size: 22px; line-height: 1; letter-spacing: 0.5px; }
  .front-brand .brand-sub { font-size: 9px; line-height: 1; letter-spacing: 0.6px; }
  .tagline {
    position: absolute; left: 33px; top: 404px;
    font-size: 20px; font-weight: 700; color: var(--white);
  }
  .tagline .accent { color: var(--sky); }

  .contact-block { position: absolute; left: 61px; top: 104px; color: var(--ink); }
  .person-name {
    font-size: 30px; font-weight: 900; color: var(--navy); letter-spacing: 0.3px; line-height: 1;
  }
  .person-org { font-size: 18px; margin-top: 8px; }
  .contact-list { list-style: none; margin-top: 26px; font-size: 16px; }
  .contact-list li { display: flex; align-items: flex-start; gap: 13px; margin-bottom: 7px; line-height: 19px; }
  .contact-list svg { width: 16px; height: 16px; flex: none; margin-top: 2px; fill: var(--navy); }

  .divider {
    position: absolute; left: 364px; top: 40px; width: 2px; height: 380px;
    background: linear-gradient(to bottom, transparent, #bdbdbd 20%, #bdbdbd 80%, transparent);
    box-shadow: 18px 0 30px rgba(0,0,0,0.12);
  }
  .back-brand {
    position: absolute; left: 450px; width: 300px; top: 125px;
    display: flex; flex-direction: column; align-items: center; gap: 12px;
    color: var(--navy); font-weight: 900; text-align: center;
  }
  .back-brand .mark-dot {
    width: 150px; height: 150px; border-radius: 50%; border: 2px solid var(--navy);
  }
  .back-brand .brand-name { font-size: 44px; line-height: 1; }
  .back-brand .brand-sub { font-size: 17px; line-height: 1; letter-spacing: 0.6px; }
</style>
</head>
<body>
<main class="canvas">
  <section class="card card-front">
    <div class="front-pattern" role="img" aria-label="Faint repeating brand pattern in navy tones"></div>
    <div class="front-brand">
      <span class="mark-dot"></span>
      <span class="brand-name">BROOKFERN</span>
      <span class="brand-sub">VETERINARY HOSPITAL</span>
    </div>
    <p class="tagline">Life Long Companions, <span class="accent">Lifelong Care</span> —</p>
  </section>

  <section class="card card-back">
    <div class="contact-block">
      <h1 class="person-name">DR. NORA HALE</h1>
      <p class="person-org">Brookfern Veterinary Hospital</p>
      <ul class="contact-list">
        <li>
          <svg viewBox="0 0 16 16" aria-hidden="true"><path d="M3.5 1l2.5 3-1.5 2c1 2 3 4 5 5l2-1.5 3 2.5-1.5 2.5C7 14 2 9 1 2.5z"/></svg>
          044-555 010 234
        </li>
        <li>
          <svg viewBox="0 0 16 16" aria-hidden="true"><path d="M1 3h14v1.5L8 9 1 4.5z M1 6l7 4.5L15 6v7H1z"/></svg>
          hello@brookfernvet.com
        </li>
        <li>
          <svg viewBox="0 0 16 16" aria-hidden="true"><path d="M8 1a7 7 0 100 14A7 7 0 008 1zm0 1.5c.8 0 1.7 1.6 2 4H6c.3-2.4 1.2-4 2-4zM2.6 6.5h2.1c0 .5-.1 1-.1 1.5s0 1 .1 1.5H2.6a5.5 5.5 0 010-3zm3.4 3h4c-.3 2.4-1.2 4-2 4s-1.7-1.6-2-4zm5.3 0c0-.5.1-1 .1-1.5s0-1-.1-1.5h2.1a5.5 5.5 0 010 3z"/></svg>
          www.brookfernvet.com
        </li>
        <li>
          <svg viewBox="0 0 16 16" aria-hidden="true"><path d="M8 1a4.5 4.5 0 00-4.5 4.5C3.5 9 8 15 8 15s4.5-6 4.5-9.5A4.5 4.5 0 008 1zm0 6.3a1.8 1.8 0 110-3.6 1.8 1.8 0 010 3.6z"/></svg>
          <span>412 Alder Ridge Rd<br>Maplewood, FL 33520,<br>7260 Willow Creek Pkwy<br>Cedar Bay, FL 33915</span>
        </li>
      </ul>
    </div>
    <div class="divider"></div>
    <div class="back-brand">
      <span class="mark-dot"></span>
      <span class="brand-name">BROOKFERN</span>
      <span class="brand-sub">VETERINARY HOSPITAL</span>
    </div>
  </section>
</main>
</body>
</html>
```